Podcastcover
Zielgruppe
Wir sind eine KI Firma und möchten einen Podcast starten. Unsere Zielgruppe sind CEO´s, CTO`s, IT-Entscheider und Beratungsunternehmen. Hierzu benötigen wir ein cooles und ausfälliges Cover.
Der Name des Podcast ist : KI Wolkenrand
Aufgabenstellung
Hoher Wiedererkennungswert
Folgendes Bild soll mit auf das Cover

```html
<!DOCTYPE html>
<html lang="de">
<head>
<meta charset="utf-8">
<title>KI Wolkenrand – Podcast Cover</title>
<link rel="stylesheet" href="https://fonts.googleapis.com/css2?family=Archivo+Black&family=Montserrat:wght@800&family=Raleway:wght@400&display=swap">
<style>
  :root {
    --mint: #12e07e;
    --ink: #1d1d1b;
    --magenta: #e046c8;
    --coral-red: #f2326e;
    --coral-dot: #f25a4a;
    --violet: #3e3f7c;
    --skin: #d4d5bf;
    --lavender: #9a98d8;
  }
  html, body {
    margin: 0;
    padding: 0;
    width: 1200px;
    height: 1200px;
    overflow: hidden;
    background: var(--mint);
  }
  .cover {
    position: relative;
    width: 1200px;
    height: 1200px;
    background: var(--mint);
    overflow: hidden;
  }
  .cover-art {
    position: absolute;
    inset: 0;
    width: 1200px;
    height: 1200px;
  }
  .label-podcast {
    position: absolute;
    left: 32px;
    top: 30px;
    margin: 0;
    font-family: "Raleway", sans-serif;
    font-weight: 400;
    font-size: 118px;
    line-height: 1;
    letter-spacing: 2px;
    color: var(--ink);
  }
  .brand {
    position: absolute;
    right: 52px;
    top: 42px;
    display: flex;
    align-items: center;
    gap: 22px;
  }
  .brand-dot {
    width: 38px;
    height: 38px;
    border-radius: 50%;
    background: var(--coral-dot);
  }
  .brand-name {
    font-family: "Montserrat", sans-serif;
    font-weight: 800;
    font-size: 112px;
    line-height: 1;
    letter-spacing: 14px;
    color: var(--ink);
  }
  .show-title {
    position: absolute;
    left: 30px;
    bottom: 62px;
    margin: 0;
    color: var(--ink);
    font-family: "Archivo Black", sans-serif;
    line-height: 1;
  }
  .show-title-main {
    display: block;
    font-size: 300px;
    letter-spacing: -6px;
    line-height: 0.82;
  }
  .show-title-sub {
    display: block;
    margin-top: 26px;
    font-size: 50px;
    letter-spacing: 3px;
  }
</style>
</head>
<body>
<main class="cover">
  <svg class="cover-art" viewBox="0 0 1200 1200" xmlns="http://www.w3.org/2000/svg">
    <defs>
      <linearGradient id="portrait-tones" x1="0" y1="0" x2="0.6" y2="1">
        <stop offset="0" stop-color="#3e3f7c"/>
        <stop offset="0.45" stop-color="#d4d5bf"/>
        <stop offset="1" stop-color="#9a98d8"/>
      </linearGradient>
    </defs>
    <circle class="backdrop-circle" cx="930" cy="640" r="460" fill="var(--coral-red)"/>
    <polygon class="backdrop-triangle" points="118,482 930,225 660,1150" fill="var(--magenta)"/>
    <g class="side-stripes" fill="var(--coral-red)">
      <polygon points="1150,560 1200,530 1200,560 1150,590"/>
      <polygon points="1150,620 1200,590 1200,620 1150,650"/>
      <polygon points="1150,680 1200,650 1200,680 1150,710"/>
      <polygon points="1150,740 1200,710 1200,740 1150,770"/>
    </g>
    <path class="portrait" role="img" aria-label="Gezeichnete Karikatur des Podcast-Hosts mit violett-magentafarbenem Haar"
      d="M360,420 C380,250 520,160 700,170 C880,175 1060,240 1140,380 C1200,480 1200,620 1200,700 L1200,1200 L720,1200 C700,1120 640,1060 560,1030 C470,990 430,900 420,820 C380,720 340,560 360,420 Z"
      fill="url(#portrait-tones)"/>
    <g class="bottom-dashes" fill="var(--ink)">
      <polygon points="0,1178 60,1178 40,1200 0,1200"/>
      <polygon points="92,1178 172,1178 152,1200 72,1200"/>
      <polygon points="204,1178 284,1178 264,1200 184,1200"/>
      <polygon points="316,1178 396,1178 376,1200 296,1200"/>
      <polygon points="428,1178 508,1178 488,1200 408,1200"/>
    </g>
  </svg>

  <p class="label-podcast">PODCAST</p>

  <div class="brand">
    <span class="brand-dot"></span>
    <span class="brand-name">NOVA</span>
  </div>

  <h1 class="show-title">
    <span class="show-title-main">KI</span>
    <span class="show-title-sub">WOLKENRAND</span>
  </h1>
</main>
</body>
</html>
```